" Trabalhamos com vistorias profissionais de imóveis. Um vistoriador (engenheiro civil ou alguém com experiência em obras e entregas de imóveis) analisa detalhadamente o imóvel, buscando e relatando vícios construtivos. Todo trabalho é documentado através de relatório, que servirá de garantia futura para as partes interessadas. Nossa ideia principal é a de que vistoriar corretamente um imóvel pode significar enorme economia e evitar muita dor de cabeça futura. "

```html
<!DOCTYPE html>
<html lang="pt-BR">
<head>
<meta charset="UTF-8">
<title>Inspecta Lar – Papel Timbrado</title>
<link rel="stylesheet" href="https://fonts.googleapis.com/css2?family=Montserrat:wght@400;600;800&display=swap">
<style>
  :root {
    --backdrop: #ececec;
    --paper: #ffffff;
    --navy: #1f2a5a;
    --accent: #e8912a;
    --mark-grey: #e7e7e8;
    --text: #2b2f3d;
  }
  * { box-sizing: border-box; margin: 0; padding: 0; }
  html, body {
    width: 1200px;
    height: 1200px;
    overflow: hidden;
    background: var(--backdrop);
    font-family: "Montserrat", sans-serif;
  }
  .letterhead {
    position: absolute;
    left: 270px;
    top: 135px;
    width: 660px;
    height: 930px;
    background: var(--paper);
    box-shadow: 0 6px 18px rgba(0,0,0,0.12);
  }
  .brand {
    position: absolute;
    top: 62px;
    left: 0;
    width: 100%;
    display: flex;
    justify-content: center;
    align-items: center;
    gap: 10px;
  }
  .brand-dot {
    width: 26px;
    height: 26px;
    border-radius: 50%;
    background: var(--navy);
  }
  .brand-name {
    font-weight: 800;
    font-size: 36px;
    letter-spacing: 0.5px;
    color: var(--navy);
  }
  .watermark-shape {
    position: absolute;
    left: 28px;
    top: 488px;
    width: 326px;
    height: 326px;
    border-radius: 50%;
    background: var(--mark-grey);
  }
  .footer-rule {
    position: absolute;
    left: 24px;
    right: 24px;
    top: 852px;
    height: 2px;
    background: var(--navy);
  }
  .footer {
    position: absolute;
    left: 24px;
    right: 24px;
    top: 866px;
    display: flex;
    justify-content: space-between;
    align-items: flex-start;
    font-size: 12px;
    color: var(--text);
  }
  .footer-phone { padding-top: 8px; }
  .footer-address { text-align: center; line-height: 1.45; }
  .footer-site {
    padding-top: 8px;
    font-weight: 600;
    display: flex;
    align-items: center;
    gap: 6px;
  }
  .footer-site .social-dot {
    width: 11px;
    height: 11px;
    border-radius: 50%;
    background: var(--navy);
  }
</style>
</head>
<body>
  <main class="letterhead">
    <header class="brand">
      <span class="brand-dot"></span>
      <span class="brand-name">INSPECTA LAR</span>
    </header>

    <div class="watermark-shape" aria-hidden="true"></div>

    <div class="footer-rule"></div>
    <footer class="footer">
      <span class="footer-phone">+ 55 00 0000 - 0000</span>
      <address class="footer-address" style="font-style:normal">
        Endereço Nome Rua, 0000<br>
        00000 - 000 Bairro / UF - Brasil
      </address>
      <span class="footer-site">inspectalar.com.br <span class="social-dot"></span></span>
    </footer>
  </main>
</body>
</html>
```